Graphics for a 'guess the color' mobile phone project

I need the graphics (including source graphics in Illustrator or Photoshop) for the screens inside the game.

Please read the attached brief carefully, thanks!

```html
<!DOCTYPE html>
<html lang="en">
<head>
<meta charset="utf-8">
<title>Guess the Color – Level Screen</title>
<link rel="stylesheet" href="https://fonts.googleapis.com/css2?family=Playfair+Display:wght@700&display=swap">
<style>
  :root {
    --backdrop: #3d3f48;
    --screen: #ffffff;
    --yellow: #ffc800;
    --orange: #ff5f12;
    --purple: #7b3590;
    --cyan: #0097c2;
    --green: #74b800;
    --magenta: #e2037f;
    --navy: #3a4c98;
    --red: #fc1d1d;
    --dark-seg: #3d3d3d;
    --mid-seg: #757575;
    --ring-grey: #bdbdbd;
    --icon-grey: #7a7a7a;
    --title-ink: #3d3d3d;
  }
  html, body {
    margin: 0;
    padding: 0;
    width: 960px;
    height: 1200px;
    overflow: hidden;
    background: var(--backdrop);
  }
  .game-screen {
    display: block;
    width: 960px;
    height: 1200px;
  }
  .level-title {
    font-family: "Playfair Display", serif;
    font-weight: 700;
    fill: var(--title-ink);
  }
  .lives-count {
    font-family: "Playfair Display", serif;
    font-weight: 700;
    fill: #ffffff;
  }
  .seg-yellow { fill: var(--yellow); }
  .seg-mid { fill: var(--mid-seg); }
  .seg-dark { fill: var(--dark-seg); }
</style>
</head>
<body>
<svg class="game-screen" viewBox="0 0 1200 1500" xmlns="http://www.w3.org/2000/svg">
  <defs>
    <filter id="screen-shadow" x="-10%" y="-10%" width="120%" height="120%">
      <feDropShadow dx="0" dy="6" stdDeviation="14" flood-color="#000" flood-opacity="0.35"/>
    </filter>
    <filter id="glow-blur" x="-10%" y="-50%" width="120%" height="200%">
      <feGaussianBlur stdDeviation="14"/>
    </filter>
    <linearGradient id="rainbow" x1="0" y1="0" x2="1" y2="0">
      <stop offset="0" stop-color="#ff6f6f"/>
      <stop offset="0.15" stop-color="#ffff00"/>
      <stop offset="0.35" stop-color="#66ff66"/>
      <stop offset="0.55" stop-color="#66ffff"/>
      <stop offset="0.75" stop-color="#9a9aff"/>
      <stop offset="1" stop-color="#ff88ff"/>
    </linearGradient>
    <clipPath id="screen-clip">
      <rect x="216" y="112" width="768" height="1280"/>
    </clipPath>
    <path id="wheel-segment" d="M -60.3 -225.1 A 233 233 0 0 1 60.3 -225.1 L 26.1 -97.6 A 101 101 0 0 0 -26.1 -97.6 Z"/>
  </defs>

  <!-- screen -->
  <rect class="screen-panel" x="216" y="112" width="768" height="1280" fill="var(--screen)" filter="url(#screen-shadow)"/>

  <!-- header rainbow glow -->
  <g class="header-glow" clip-path="url(#screen-clip)">
    <path d="M 200 300 Q 600 400 1000 300" fill="none" stroke="url(#rainbow)" stroke-width="36" filter="url(#glow-blur)" opacity="0.75"/>
    <path d="M 216 112 H 984 V 278 Q 600 400 216 278 Z" fill="var(--screen)"/>
  </g>

  <!-- lives heart -->
  <g class="lives-heart" transform="translate(345 212)">
    <path d="M 0 56 C -40 30 -66 8 -64 -22 C -62 -48 -40 -58 -22 -56 C -10 -55 -3 -48 0 -42 C 3 -48 10 -55 22 -56 C 40 -58 62 -48 64 -22 C 66 8 40 30 0 56 Z" fill="#a90000"/>
    <path d="M 0 44 C -34 22 -54 4 -52 -20 C -50 -40 -34 -47 -20 -45 C -10 -44 -3 -38 0 -32 C 3 -38 10 -44 20 -45 C 34 -47 50 -40 52 -20 C 54 4 34 22 0 44 Z" fill="#f21c1c"/>
    <text class="lives-count" x="0" y="20" font-size="60" text-anchor="middle">5</text>
  </g>

  <!-- level title -->
  <g class="level-badge">
    <text class="level-title" x="598" y="218" font-size="50" text-anchor="middle">Solve it</text>
    <text class="level-title" x="598" y="292" font-size="64" text-anchor="middle">5</text>
  </g>

  <!-- shop button -->
  <g class="shop-button" transform="translate(850 208)">
    <circle r="58" fill="none" stroke="var(--ring-grey)" stroke-width="12"/>
    <circle r="58" fill="none" stroke="#555" stroke-width="12" stroke-dasharray="30 16.4"/>
    <circle r="50" fill="#fff"/>
    <path d="M -36 -22 C -26 -26 -20 -18 -16 -6 C -12 8 -2 16 12 16 C 26 16 34 8 36 -2" fill="none" stroke="var(--icon-grey)" stroke-width="5" stroke-linecap="round"/>
    <circle cx="-12" cy="26" r="3" fill="var(--icon-grey)"/>
    <circle cx="32" cy="26" r="3" fill="var(--icon-grey)"/>
    <path d="M 2 12 L -6 4 A 5 5 0 0 1 2 -3 A 5 5 0 0 1 10 4 Z" fill="var(--icon-grey)"/>
    <polygon points="20,-22 23,-14 31,-14 25,-9 27,-1 20,-6 13,-1 15,-9 9,-14 17,-14" fill="var(--icon-grey)"/>
  </g>

  <!-- help button -->
  <g class="help-button" transform="translate(858 413)">
    <path d="M -34 46 L -40 66 L -14 56 Z" fill="var(--icon-grey)"/>
    <circle r="50" fill="none" stroke="var(--ring-grey)" stroke-width="12"/>
    <circle r="50" fill="none" stroke="#555" stroke-width="12" stroke-dasharray="26 14"/>
    <circle r="43" fill="#fff"/>
    <path d="M -16 -12 A 18 18 0 1 1 6 6 C -4 12 -8 18 -8 24" fill="none" stroke="var(--icon-grey)" stroke-width="5" stroke-linecap="round"/>
    <circle cx="-8" cy="32" r="3.5" fill="var(--icon-grey)"/>
  </g>

  <!-- colour wheel -->
  <g class="colour-wheel" transform="translate(595 640)">
    <use href="#wheel-segment" class="seg-yellow" transform="rotate(0)"/>
    <use href="#wheel-segment" class="seg-mid" transform="rotate(30)"/>
    <use href="#wheel-segment" class="seg-dark" transform="rotate(60)"/>
    <use href="#wheel-segment" class="seg-yellow" transform="rotate(90)"/>
    <use href="#wheel-segment" class="seg-mid" transform="rotate(120)"/>
    <use href="#wheel-segment" class="seg-dark" transform="rotate(150)"/>
    <use href="#wheel-segment" class="seg-yellow" transform="rotate(180)"/>
    <use href="#wheel-segment" class="seg-mid" transform="rotate(210)"/>
    <use href="#wheel-segment" class="seg-dark" transform="rotate(240)"/>
    <use href="#wheel-segment" class="seg-yellow" transform="rotate(270)"/>
    <use href="#wheel-segment" class="seg-mid" transform="rotate(300)"/>
    <use href="#wheel-segment" class="seg-dark" transform="rotate(330)"/>
  </g>

  <!-- answer slots -->
  <g class="answer-slots">
    <circle cx="506" cy="957" r="26" fill="none" stroke="var(--yellow)" stroke-width="16"/>
    <circle cx="506" cy="957" r="34" fill="none" stroke="#e0ac00" stroke-width="1.5"/>
    <circle cx="597" cy="957" r="26" fill="none" stroke="#e3e3e3" stroke-width="16"/>
    <circle cx="597" cy="957" r="34" fill="none" stroke="#c8c8c8" stroke-width="1.5"/>
    <circle cx="688" cy="957" r="26" fill="none" stroke="#e3e3e3" stroke-width="16"/>
    <circle cx="688" cy="957" r="34" fill="none" stroke="#c8c8c8" stroke-width="1.5"/>
  </g>

  <!-- colour palette -->
  <g class="colour-palette" fill="none" stroke-width="33">
    <circle cx="387" cy="1100" r="43.5" stroke="var(--yellow)"/>
    <circle cx="528" cy="1100" r="43.5" stroke="var(--orange)"/>
    <circle cx="669" cy="1100" r="43.5" stroke="var(--purple)"/>
    <circle cx="809" cy="1100" r="43.5" stroke="var(--cyan)"/>
    <circle cx="387" cy="1246" r="43.5" stroke="var(--green)"/>
    <circle cx="528" cy="1246" r="43.5" stroke="var(--magenta)"/>
    <circle cx="669" cy="1246" r="43.5" stroke="var(--navy)"/>
    <circle cx="809" cy="1246" r="43.5" stroke="var(--red)"/>
  </g>
  <g class="palette-marks">
    <circle cx="387" cy="1100" r="16" fill="#a8a8a8"/>
    <path d="M 518 1090 L 538 1110 M 538 1090 L 518 1110" stroke="#a8a8a8" stroke-width="7" stroke-linecap="round"/>
  </g>
</svg>
</body>
</html>
```